Talbrin Business Cards

Front and back. Simon Kavelle MBA is the CEO of Talbrin Homes. Black white and grays. Logo and cool design.

Target Market(s)

Professional lenders and investors

Industry/Entity Type

Real estate developer. NO HOUSES OR ROOFS

Contact Information for Business Card

Logo, name and unique design. Front and back. Simon Kavelle MBA is the CEO of Talbrin Homes. Black white and grays. Logo and cool design.

Font styles to use
Sans Serif

Colors

Designer to choose only greyscale colors for use in the design.

Requirements
Must have
• Cool look. Not the same card I could design.
Nice to have
• Something memorable
Should not have
• Basic

```html
<!DOCTYPE html>
<html lang="en">
<head>
<meta charset="utf-8">
<title>Talbrin Homes Business Cards</title>
<link rel="stylesheet" href="https://fonts.googleapis.com/css2?family=Open+Sans:wght@400;700;800&display=swap">
<style>
  :root {
    --backdrop: #3a3a3a;
    --card: #141414;
    --ink: #ffffff;
    --ink-soft: #e6e6e6;
  }
  * { box-sizing: border-box; margin: 0; padding: 0; }
  html, body { width: 1200px; height: 689px; overflow: hidden; }
  body {
    background: var(--backdrop);
    font-family: "Open Sans", Arial, sans-serif;
    color: var(--ink);
    position: relative;
  }
  .card {
    position: absolute;
    top: 190px;
    width: 540px;
    height: 309px;
    background: var(--card);
    border-radius: 22px;
  }
  .card--front { left: 40px; }
  .card--back { left: 620px; }

  .wordmark {
    position: absolute;
    text-align: center;
    font-weight: 800;
    color: var(--ink);
    line-height: 1;
  }
  .card--front .wordmark { left: 0; right: 0; top: 92px; }
  .card--back .wordmark { left: 40px; width: 320px; top: 40px; }
  .wordmark__name { display: block; letter-spacing: -2px; }
  .card--front .wordmark__name { font-size: 96px; }
  .card--back .wordmark__name { font-size: 66px; }
  .wordmark__sub { display: block; font-weight: 800; letter-spacing: 14px; padding-left: 14px; }
  .card--front .wordmark__sub { font-size: 20px; margin-top: 6px; }
  .card--back .wordmark__sub { font-size: 14px; margin-top: 4px; letter-spacing: 10px; padding-left: 10px; }

  .identity { position: absolute; left: 40px; width: 320px; top: 160px; text-align: center; }
  .identity__name { font-weight: 700; font-size: 20px; }
  .identity__role { font-size: 14px; color: var(--ink-soft); margin-top: 2px; }

  .details {
    position: absolute;
    left: 40px; right: 30px; top: 222px;
    display: flex; align-items: center; gap: 22px;
  }
  .address { font-size: 14px; line-height: 1.5; text-align: center; color: var(--ink-soft); width: 170px; }
  .divider { width: 1px; height: 56px; background: var(--ink); }
  .contacts { list-style: none; font-size: 14px; line-height: 1.55; color: var(--ink-soft); }
  .contacts li { display: flex; align-items: center; gap: 8px; }
  .contacts svg { width: 12px; height: 12px; fill: var(--ink); flex: none; }
</style>
</head>
<body>
  <section class="card card--front" aria-label="Card front">
    <div class="wordmark">
      <span class="wordmark__name">Talbrin</span>
      <span class="wordmark__sub">HOMES</span>
    </div>
  </section>

  <section class="card card--back" aria-label="Card back">
    <div class="wordmark">
      <span class="wordmark__name">Talbrin</span>
      <span class="wordmark__sub">HOMES</span>
    </div>
    <div class="identity">
      <p class="identity__name">Simon Kavelle MBA</p>
      <p class="identity__role">CEO of Talbrin Homes</p>
    </div>
    <div class="details">
      <p class="address">Your address, City<br>State, Zip 1234</p>
      <span class="divider"></span>
      <ul class="contacts">
        <li>
          <svg viewBox="0 0 24 24" aria-hidden="true"><path d="M6.6 10.8a15 15 0 0 0 6.6 6.6l2.2-2.2c.3-.3.7-.4 1-.2 1.1.4 2.3.6 3.6.6.6 0 1 .4 1 1V20c0 .6-.4 1-1 1A17 17 0 0 1 3 4c0-.6.4-1 1-1h3.5c.6 0 1 .4 1 1 0 1.3.2 2.5.6 3.6.1.3 0 .7-.2 1z"/></svg>
          123 456 789
        </li>
        <li>
          <svg viewBox="0 0 24 24" aria-hidden="true"><path d="M2 5h20v14H2z M2 5l10 8 10-8" /></svg>
          info@youremail.com
        </li>
        <li>
          <svg viewBox="0 0 24 24" aria-hidden="true"><circle cx="12" cy="12" r="10"/></svg>
          www.yourwebsite.com
        </li>
      </ul>
    </div>
  </section>
</body>
</html>
```